Business Card for TLK Field Services

Would like a large logo on one side. On the other side, logo on one side and company phone number, address, and email on the other side. I don't have a logo so please create one for us.
Updates
I don't have a logo, so please create one for us.
Target Market(s)
Land Surveying
Industry/Entity Type
Surveyor
Contact Information for Business Card
Would like a large logo on one side. On the other side, logo on one side and company phone number, address, and email on the other side
Requirements
Nice to have
- would like the initials to be incorporated with the logo

```html
<!DOCTYPE html>
<html lang="en">
<head>
<meta charset="utf-8">
<title>TLK Field Services – Business Cards</title>
<link rel="stylesheet" href="https://fonts.googleapis.com/css2?family=Arimo:wght@400;700&display=swap">
<style>
  :root {
    --backdrop: #1b1b1b;
    --brand-red: #b3242a;
    --brand-red-deep: #a11f25;
    --card-white: #ececec;
    --ink-white: #ffffff;
  }
  * { box-sizing: border-box; margin: 0; padding: 0; }
  html, body { width: 1200px; height: 800px; overflow: hidden; }
  body {
    background: var(--backdrop);
    font-family: "Arimo", Arial, sans-serif;
    position: relative;
  }
  .card {
    position: absolute;
    width: 500px;
    height: 286px;
    border-radius: 3px;
    overflow: hidden;
    box-shadow: 0 18px 40px rgba(0,0,0,.55);
  }
  .card--front {
    left: 90px;
    top: 420px;
    background: var(--brand-red);
    display: flex;
    align-items: center;
    justify-content: center;
  }
  .card--back {
    left: 610px;
    top: 110px;
    display: flex;
  }
  .brand-mark {
    display: flex;
    align-items: center;
    font-weight: 700;
    white-space: nowrap;
    line-height: 1;
  }
  .brand-mark__dot {
    border-radius: 50%;
    border-style: solid;
    border-color: currentColor;
    flex: none;
  }
  .card--front .brand-mark {
    color: var(--ink-white);
    font-size: 31px;
    gap: 16px;
  }
  .card--front .brand-mark__dot {
    width: 120px;
    height: 120px;
    border-width: 6px;
  }
  .card__logo-panel {
    width: 44%;
    background: var(--card-white);
    display: flex;
    align-items: center;
    justify-content: center;
  }
  .card__logo-panel .brand-mark {
    color: var(--brand-red);
    font-size: 15px;
    gap: 8px;
  }
  .card__logo-panel .brand-mark__dot {
    width: 52px;
    height: 52px;
    border-width: 3px;
  }
  .card__info-panel {
    width: 56%;
    background: linear-gradient(160deg, var(--brand-red) 0%, var(--brand-red-deep) 100%);
    color: var(--ink-white);
    padding: 40px 24px 0 28px;
  }
  .contact__name { font-size: 17px; font-weight: 700; }
  .contact__title { font-size: 13px; margin-top: 3px; }
  .contact__details { margin-top: 46px; font-size: 13px; line-height: 1.55; }
</style>
</head>
<body>
  <section class="card card--back" aria-label="Business card, contact side">
    <div class="card__logo-panel">
      <div class="brand-mark"><span class="brand-mark__dot"></span>TLK Field Services</div>
    </div>
    <div class="card__info-panel">
      <p class="contact__name">Your Name goes here</p>
      <p class="contact__title">Your Title goes here</p>
      <div class="contact__details">
        <p>Your Address goes<br>here ......................</p>
        <p>p: 0123456789</p>
        <p>e: yourname@tlkmail.com</p>
      </div>
    </div>
  </section>

  <section class="card card--front" aria-label="Business card, logo side">
    <div class="brand-mark"><span class="brand-mark__dot"></span>TLK Field Services</div>
  </section>
</body>
</html>
```